Video Company Business Card Design

We are looking for a new design for business cards that will complement our new logo and new website design.

Target Market(s)

professionals who need video work done

Industry/Entity Type

Business

Requirements
Must have
• Logo
compliment website look seen here...http://k7pixelworks.example/brightlane/

info for card:
Dana Whitlow
Producer/ Cinematographer

532 Pellingham NE
Harlow Falls, ZZ 00000
(inside The RAVN Hall)
(485) 555-0142
Dana@brightlanemedia.example
www.brightlanemedia.example

```html
<!DOCTYPE html>
<html lang="en">
<head>
<meta charset="UTF-8">
<title>BrightLane Media – Business Card</title>
<link rel="stylesheet" href="https://fonts.googleapis.com/css2?family=Montserrat:wght@400;500&display=swap">
<style>
  :root {
    --stage: #1c1c1e;
    --front-top: #235e5f;
    --front-bottom: #11393b;
    --back-card: #2b2b2d;
    --brand-green: #3fa84a;
    --text-light: #e6e6e6;
    --text-muted: #cfcfcf;
  }
  * { margin: 0; padding: 0; box-sizing: border-box; }
  html, body {
    width: 1200px;
    height: 900px;
    overflow: hidden;
    background: var(--stage);
    font-family: "Montserrat", Arial, sans-serif;
  }
  .card-set {
    position: absolute;
    inset: 0;
    display: flex;
    align-items: center;
    justify-content: center;
    gap: 56px;
  }
  .card {
    position: relative;
    width: 525px;
    height: 300px;
    border-radius: 18px;
    overflow: hidden;
    box-shadow: 0 12px 30px rgba(0,0,0,.55);
  }
  /* Front */
  .card--front {
    background: linear-gradient(160deg, var(--front-top), var(--front-bottom));
  }
  .brand {
    display: flex;
    align-items: center;
    gap: 8px;
    color: var(--brand-green);
    font-weight: 500;
    text-transform: uppercase;
    letter-spacing: 0.5px;
    white-space: nowrap;
  }
  .brand__square {
    width: 0.75em;
    height: 0.75em;
    background: var(--brand-green);
  }
  .card--front .brand {
    position: absolute;
    left: 60px;
    top: 110px;
    font-size: 32px;
  }
  .tagline {
    position: absolute;
    left: 62px;
    top: 172px;
    color: var(--text-light);
    font-size: 13px;
    letter-spacing: 2.5px;
    text-transform: uppercase;
  }
  /* Back */
  .card--back { background: var(--back-card); }
  .card--back .brand {
    position: absolute;
    right: 34px;
    top: 30px;
    font-size: 26px;
  }
  .person {
    position: absolute;
    left: 34px;
    top: 120px;
  }
  .person__name {
    color: var(--brand-green);
    font-size: 19px;
    font-weight: 400;
    letter-spacing: 1px;
    text-transform: uppercase;
  }
  .person__title {
    color: var(--text-light);
    font-size: 14px;
    margin-top: 4px;
  }
  .rule {
    position: absolute;
    left: 34px;
    right: 34px;
    top: 176px;
    height: 1px;
    background: var(--brand-green);
  }
  .contact {
    position: absolute;
    left: 34px;
    top: 192px;
    font-size: 13.5px;
    line-height: 1.6;
    color: var(--text-light);
    font-style: normal;
  }
  .contact__web { color: var(--brand-green); }
  .address {
    position: absolute;
    right: 34px;
    top: 192px;
    font-size: 13.5px;
    line-height: 1.6;
    color: var(--text-muted);
    font-style: normal;
  }
</style>
</head>
<body>
  <main class="card-set">
    <section class="card card--front" aria-label="Card front">
      <div class="brand"><span>BrightLane Media</span><span class="brand__square"></span></div>
      <p class="tagline">Picture. Shape. Deliver.</p>
    </section>

    <section class="card card--back" aria-label="Card back">
      <div class="brand"><span>BrightLane Media</span><span class="brand__square"></span></div>
      <div class="person">
        <h1 class="person__name">Dana Whitlow</h1>
        <p class="person__title">Producer/ Cinematographer</p>
      </div>
      <div class="rule"></div>
      <address class="contact">
        (485) 555-0142<br>
        Dana@brightlanemedia.example<br>
        <span class="contact__web">www.brightlanemedia.example</span>
      </address>
      <address class="address">
        532 Pellingham NE<br>
        Harlow Falls, ZZ 00000<br>
        (inside The RAVN Hall)
      </address>
    </section>
  </main>
</body>
</html>
```